Bring to life the sophistication and high-level expertise of my consulting business

I am looking for a sleek, modern, sharp PowerPoint design package, with options for a wide range of slide types.
We would like our logo/graphic and its colors (a blue pallet) to be prominently featured. The design should communicate expertise, sophistication, executive-level of work, be bold and look clean and sleek at the same time. There should be no doubt this was professionally done.
The font that will best work with this logo is a basic font using AvantGarde BkBt (custom)
Company briefing:
A consulting and advisory practice specialized in the Consumer Goods and Services Industries. Our methodology is distinguished by its ability to transform visionary thinking—be it blue-sky ideas, inspiration, or innovation—into practical strategies. We drive initiatives aimed at driving revenue growth and enhancing profit margins using 3 pillars: THE PEOPLE, THE CUSTOMER EXPERIENCE and THE OPERATING PLATFORM.
Target audiences are in 3 key areas: C-suite executives (owners and decision-makers of small to mid-cap companies), partners in larger Consulting Companies and Investment Firms (Private Equity/Venture capital, etc)

*In addition to the PowerPoint package, I would like a quote for designs for an email signature, a Microsoft Word template, and a company Pronetix page (all in the same style as the PPT template)

Low design quality

Target Market(s)

Target audiences are in 3 key areas: C-suite executives (owners and decision-makers), partners in larger Consulting Companies and Investment Firms (Private Equity/Venture capital, etc.)

Industry/Entity Type

Business Consulting and Advisory

Font styles to use
Sans Serif
Other font styles liked:
• The font that will work best with the logo is basic font using AvantGarde BkBt (custom)

Colors
0054AA
0677BA
7BADD7
CADEEF
E8F1F8
0094D4
00A9DD
6FCCEA
C7EBF8
E9F6FB

Requirements
Must have
• We would like our logo, the graphic shapes and its colors (a blue pallet) to be prominently featured. The design should communicate expertise, sophistication, executive-level of work. It should be sleek, modern, bold and unique.
Nice to have
• A large number of slide options for each type of slide as part of the package
Should not have
• it should not look busy, generic or too traditional

```html
<!DOCTYPE html>
<html lang="en">
<head>
<meta charset="utf-8">
<title>Claravis PowerPoint Presentation</title>
<link href="https://fonts.googleapis.com/css2?family=Poppins:ital,wght@0,400;0,500;0,600;0,700;1,400&family=Questrial&family=Source+Sans+3:wght@700&display=swap" rel="stylesheet">
<style>
:root{
  --navy:#0054AA;
  --blue:#0677BA;
  --sky:#0094D4;
  --cyan:#00A9DD;
  --soft:#6FCCEA;
  --mist:#7BADD7;
  --pale:#C7EBF8;
  --ice:#E9F6FB;
  --page:#A6E6FC;
  --ink:#1c1f26;
  --white:#ffffff;
}
*{box-sizing:border-box;margin:0;padding:0}
html,body{width:692px;height:1200px;overflow:hidden}
body{background:var(--page);font-family:"Questrial",sans-serif;color:var(--ink);position:relative}
.sheet-title{position:absolute;left:0;top:18px;width:692px;text-align:center;font-family:"Source Sans 3",sans-serif;font-weight:700;line-height:1.12;color:#15171c}
.sheet-title .line1{font-size:29px;letter-spacing:-0.3px;display:block}
.sheet-title .line2{font-size:29px;display:block}

.slot{position:absolute;width:304px;height:171px;overflow:hidden}
.slide{position:absolute;left:0;top:0;width:640px;height:360px;transform:scale(.475);transform-origin:0 0;background:var(--white);overflow:hidden}

/* shared slide parts */
.head-mark{position:absolute;left:18px;top:34px;width:52px;height:22px}
.slide-title{position:absolute;left:82px;top:10px;font-family:"Poppins",sans-serif;font-weight:700;font-size:37px;color:var(--blue);letter-spacing:-.3px;white-space:nowrap}
.slide-sub{position:absolute;left:84px;top:62px;font-size:19px;color:var(--sky);white-space:nowrap}
.logo{position:absolute;right:18px;top:30px;display:flex;align-items:center;gap:6px;font-family:"Poppins",sans-serif;font-weight:500;font-size:11px;letter-spacing:3px;color:var(--blue)}
.logo-dot{width:16px;height:16px;border-radius:50%;border:2px solid var(--sky)}
.logo.light{color:var(--white);font-size:17px;letter-spacing:5px;top:40px;right:22px}
.logo.light .logo-dot{width:24px;height:24px;border-color:var(--white)}
.page-no{position:absolute;left:12px;bottom:10px;width:26px;height:26px;border-radius:50%;border:2px solid var(--blue);background:var(--white);font-size:11px;color:var(--navy);display:flex;align-items:center;justify-content:center}
.photo{position:absolute;background:linear-gradient(135deg,#8a8f98,#4f5866 60%,#2f3a4a)}
.photo.round{border-radius:50%}
.pattern{position:absolute;border-radius:50%;background:radial-gradient(circle,rgba(0,148,212,.35) 0%,rgba(111,204,234,.25) 45%,rgba(199,235,248,0) 72%)}
.lorem{font-size:10.5px;line-height:1.32;color:#333;text-align:justify}

/* cover */
.cover{background:linear-gradient(180deg,#3b414c,#23272f)}
.cover .photo{inset:0;background:linear-gradient(160deg,#6d737d 0%,#3d434d 45%,#1f232a 100%);opacity:.9}
.cover-title{position:absolute;left:0;right:0;top:160px;text-align:center;font-family:"Poppins",sans-serif;font-weight:600;font-size:42px;color:var(--white)}
.cover-sub{position:absolute;left:0;right:0;top:220px;text-align:center;font-size:18px;color:var(--white)}

/* contents */
.contents-photo{position:absolute;left:0;top:0;width:330px;height:360px;border-radius:0 50% 50% 0/0 50% 50% 0;background:linear-gradient(150deg,#b88b4a,#6d4a2a 55%,#3c3a3e)}
.contents-word{position:absolute;left:104px;top:155px;font-family:"Poppins",sans-serif;font-weight:600;font-size:38px;color:var(--white)}
.toc-arc{position:absolute;left:270px;top:0;width:120px;height:360px}
.toc-item{position:absolute;display:flex;align-items:center;gap:6px;font-family:"Poppins",sans-serif;font-weight:500;font-size:12.5px;color:var(--ink)}
.toc-num{width:24px;height:24px;border-radius:50%;border:2px solid var(--sky);background:var(--white);color:var(--navy);font-size:13px;display:flex;align-items:center;justify-content:center}

/* intro */
.bullets{position:absolute;left:84px;top:100px;width:290px;font-family:"Poppins",sans-serif;font-weight:500;font-size:10.5px;line-height:1.35;list-style:none}
.bullets li::before{content:"• "}
.intro-copy{position:absolute;left:92px;top:160px;width:275px}

/* about */
.pill{position:absolute;left:0;width:425px;height:66px;border-radius:0 34px 34px 0;background:linear-gradient(90deg,var(--blue),var(--cyan));color:var(--white);padding:6px 0 0 30px}
.pill h3{font-family:"Poppins",sans-serif;font-weight:600;font-size:12.5px}
.pill h3::before{content:"• "}
.pill p{font-size:10px;line-height:1.3;padding-left:16px;margin-top:4px}

/* services */
.service{position:absolute;left:0;width:167px;height:66px;border-radius:0 34px 34px 0;background:linear-gradient(90deg,var(--blue),var(--sky));display:flex;align-items:center;padding-left:24px;gap:10px;color:var(--white);font-family:"Poppins",sans-serif;font-weight:500;font-size:13px}
.service-icon{width:48px;height:48px;border-radius:50%;background:var(--white);display:flex;align-items:center;justify-content:center}
.service-text{position:absolute;left:176px;width:260px;font-family:"Poppins",sans-serif;font-weight:600;font-size:12.5px;line-height:1.35;color:var(--navy)}

/* industry */
.industry-lead{position:absolute;left:26px;top:110px;width:400px;font-family:"Poppins",sans-serif;font-weight:500;font-size:10px;line-height:1.35}
.case{position:absolute;top:188px;width:150px}
.case h4{font-family:"Poppins",sans-serif;font-weight:600;font-size:12.5px;color:var(--navy);white-space:nowrap;margin-bottom:12px}
.case p{font-size:10px;line-height:1.3;color:#333}

/* methodology */
.step-num{position:absolute;top:118px;font-family:"Poppins",sans-serif;font-weight:700;font-size:56px;line-height:1}
.step{position:absolute;top:150px;width:120px;height:210px;border-radius:30px 30px 0 0;padding:40px 12px 0;font-family:"Poppins",sans-serif;font-weight:500;font-size:10px;line-height:1.3;text-align:center}

/* team */
.member{position:absolute;top:105px;width:160px;height:255px;background:linear-gradient(180deg,#e6e8ea 0%,#c9ccd0 55%,var(--blue) 100%)}
.member-label{position:absolute;left:0;right:0;bottom:18px;text-align:center;font-family:"Poppins",sans-serif;font-weight:600;font-size:14px;line-height:1.25;color:var(--white)}

/* audiences */
.audience{position:absolute;left:325px;width:290px}
.audience-icon{position:absolute;left:0;top:0;width:26px;height:30px}
.audience h4{margin-left:42px;font-family:"Poppins",sans-serif;font-weight:600;font-size:19px;color:var(--navy)}
.audience p{margin-left:42px;margin-top:6px;font-size:10px;line-height:1.3;color:#333}

/* stories */
.story-copy{position:absolute;left:25px;top:145px;width:300px;font-family:"Poppins",sans-serif;font-weight:500;font-size:11.5px;line-height:1.4}
.story-grid{position:absolute;left:350px;top:84px;width:278px;height:266px;display:grid;grid-template-columns:1fr 1fr;grid-template-rows:1fr 1fr;gap:4px}
.quote-box{background:var(--sky);border-radius:30px 0 0 0;color:var(--white);font-size:10px;line-height:1.3;text-align:center;padding:10px 14px}
.quote-mark{font-family:"Poppins",sans-serif;font-weight:700;font-size:28px;text-align:right;line-height:1}
.story-grid .cell{position:relative;background:linear-gradient(135deg,#5b6f8a,#2a3550)}
.story-grid .cell.warm{background:linear-gradient(135deg,#a58c78,#4d5260)}
.story-grid .cell.chess{border-radius:0 0 0 30px;background:linear-gradient(135deg,#1f3d8a,#0a1a44)}
.story-grid .cell.sky{background:linear-gradient(160deg,#dfe6ee,#6f7f95)}

/* video */
.play{position:absolute;left:302px;top:130px;width:40px;height:48px}
.video-label{position:absolute;left:0;right:0;top:208px;text-align:center;font-family:"Poppins",sans-serif;font-weight:600;font-size:27px;color:var(--navy)}

/* contact */
.contact-photo{position:absolute;left:0;top:0;width:360px;height:352px;border-radius:0 0 170px 170px/0 0 120px 120px;background:linear-gradient(160deg,#2c3f58,#17233a 60%,#0f1829)}
.contact-title{position:absolute;left:82px;top:10px;font-family:"Poppins",sans-serif;font-weight:700;font-size:37px;color:var(--white)}
.contact-sub{position:absolute;left:84px;top:60px;font-size:19px;color:var(--white)}
.contact-copy{position:absolute;left:52px;top:112px;width:268px;font-family:"Poppins",sans-serif;font-style:italic;font-size:11.5px;line-height:1.4;color:var(--white)}
.contact-info{position:absolute;left:405px;top:98px;width:190px;text-align:center;font-family:"Poppins",sans-serif}
.contact-info dt{font-weight:500;font-size:14px;color:var(--ink)}
.contact-info dd{font-weight:600;font-size:12px;color:var(--navy);margin-bottom:16px}
.contact-info dd::after{content:"";display:block;margin:8px auto 0;width:20px;height:4px;border-radius:2px;background:var(--sky)}
.contact-info dd:last-child::after{display:none}
</style>
</head>
<body>

<h1 class="sheet-title"><span class="line1">CLARAVIS POWER POINT PRESENTATION</span><span class="line2">modern and unique design</span></h1>

<!-- cover -->
<div class="slot" style="left:40px;top:109px">
  <section class="slide cover">
    <div class="photo" role="img" aria-label="Black and white photo of a city skyline seen through office windows"></div>
    <div class="pattern" style="left:-80px;top:-60px;width:420px;height:480px" role="img" aria-label="Blue connected-dot pattern"></div>
    <div class="logo light"><span class="logo-dot"></span><span>CLARAVIS</span></div>
    <div class="cover-title">Claravis Company</div>
    <div class="cover-sub">Specializing in Consumer Goods and Services Industries</div>
  </section>
</div>

<!-- contents -->
<div class="slot" style="left:362px;top:109px">
  <section class="slide">
    <div class="contents-photo" role="img" aria-label="Photo of hands typing on a laptop"></div>
    <div class="pattern" style="left:-40px;top:-20px;width:360px;height:400px" role="img" aria-label="Blue connected-dot pattern"></div>
    <div class="contents-word">Content</div>
    <svg class="toc-arc" viewBox="0 0 120 360"><path d="M0 0 Q150 180 0 360" fill="none" stroke="#0677BA" stroke-width="1.5"/></svg>
    <div class="logo"><span class="logo-dot"></span><span>CLARAVIS</span></div>
    <div class="toc-item" style="left:304px;top:30px"><span class="toc-num">01</span>Introduction</div>
    <div class="toc-item" style="left:328px;top:70px"><span class="toc-num">02</span>About Us</div>
    <div class="toc-item" style="left:343px;top:110px"><span class="toc-num">03</span>Our Services</div>
    <div class="toc-item" style="left:352px;top:154px"><span class="toc-num">04</span>Industry Expertise</div>
    <div class="toc-item" style="left:352px;top:199px"><span class="toc-num">05</span>Our Methodology</div>
    <div class="toc-item" style="left:342px;top:238px"><span class="toc-num">06</span>Meet Our Team</div>
    <div class="toc-item" style="left:324px;top:273px"><span class="toc-num">07</span>Target Audiences</div>
    <div class="toc-item" style="left:304px;top:309px"><span class="toc-num">08</span>Get in touch</div>
  </section>
</div>

<!-- introduction -->
<div class="slot" style="left:40px;top:287px">
  <section class="slide">
    <svg class="head-mark" viewBox="0 0 52 22"><line x1="0" y1="11" x2="30" y2="11" stroke="#0677BA" stroke-width="3"/><circle cx="8" cy="11" r="5" fill="#0677BA"/><circle cx="40" cy="11" r="11" fill="#0094D4"/></svg>
    <div class="slide-title">Introduction</div>
    <div class="slide-sub">Welcome to CLARAVIS Company</div>
    <div class="logo"><span class="logo-dot"></span><span>CLARAVIS</span></div>
    <ul class="bullets">
      <li>Brief overview of specialization in Consumer Goods and Services Industries.</li>
      <li>Introduction of key services and expertise.</li>
    </ul>
    <p class="lorem intro-copy">Lorem ipsum dolor sit amet, consectetuer adipiscing elit, sed diam nonummy nibh euismod tincidunt ut laoreet dolore magna aliquam erat volutpat. Ut wisi enim ad minim veniam, quis nostrud exerci tation ullamcorper suscipit lobortis nisl ut aliquip ex ea commodo consequat. Duis autem vel eum iriure dolor in Lorem ipsum dolor sit amet, consectetuer adipiscing elit, sed diam nonummy nibh euismod tincidunt ut laoreet dolore magna aliquam erat volutpat. Ut wisi enim ad minim veniam, quis nostrud exerci tation</p>
    <div class="pattern" style="left:380px;top:80px;width:300px;height:300px" role="img" aria-label="Blue connected-dot pattern"></div>
    <div class="photo round" style="left:432px;top:112px;width:270px;height:270px;background:linear-gradient(135deg,#d7d4cf,#8d8a86)" role="img" aria-label="Photo of people signing documents at a desk"></div>
    <div class="page-no">1</div>
  </section>
</div>

<!-- about -->
<div class="slot" style="left:362px;top:287px">
  <section class="slide">
    <svg class="head-mark" viewBox="0 0 52 22"><line x1="0" y1="11" x2="30" y2="11" stroke="#0677BA" stroke-width="3"/><circle cx="8" cy="11" r="5" fill="#0677BA"/><circle cx="40" cy="11" r="11" fill="#0094D4"/></svg>
    <div class="slide-title">About Us</div>
    <div class="slide-sub">Who we are ?</div>
    <div class="logo"><span class="logo-dot"></span><span>CLARAVIS</span></div>
    <div class="pill" style="top:94px"><h3>Overview of Claravis Consulting Company</h3><p>Lorem ipsum dolor sit amet, consectetuer adipiscing elit,<br>sed diam nonummy nibh euismod tincidunt ut laoreet</p></div>
    <div class="pill" style="top:168px"><h3>Core values that guide our approach.</h3><p>Lorem ipsum dolor sit amet, consectetuer adipiscing elit,<br>sed diam nonummy nibh euismod tincidunt ut laoreet</p></div>
    <div class="pill" style="top:242px"><h3>Mission and vision statements</h3><p>Lorem ipsum dolor sit amet, consectetuer adipiscing elit,<br>sed diam nonummy nibh euismod tincidunt ut laoreet</p></div>
    <div class="pattern" style="left:420px;top:90px;width:260px;height:290px" role="img" aria-label="Blue connected-dot pattern"></div>
    <div class="photo round" style="left:457px;top:160px;width:152px;height:152px" role="img" aria-label="Photo of a team meeting around a table"></div>
    <div class="page-no">2</div>
  </section>
</div>

<!-- services -->
<div class="slot" style="left:40px;top:465px">
  <section class="slide">
    <svg class="head-mark" viewBox="0 0 52 22"><line x1="0" y1="11" x2="30" y2="11" stroke="#0677BA" stroke-width="3"/><circle cx="8" cy="11" r="5" fill="#0677BA"/><circle cx="40" cy="11" r="11" fill="#0094D4"/></svg>
    <div class="slide-title">Our Services</div>
    <div class="slide-sub">Tailored Solutions for Success</div>
    <div class="logo"><span class="logo-dot"></span><span>CLARAVIS</span></div>
    <div class="service" style="top:94px">Service 01<span class="service-icon"><svg width="24" height="24" viewBox="0 0 24 24"><circle cx="12" cy="9" r="5" fill="none" stroke="#0677BA" stroke-width="2.5"/><path d="M3 19h7l4-2h7" fill="none" stroke="#0677BA" stroke-width="2.5"/></svg></span></div>
    <div class="service" style="top:168px">Service 02<span class="service-icon"><svg width="24" height="24" viewBox="0 0 24 24"><rect x="3" y="4" width="16" height="12" fill="none" stroke="#0677BA" stroke-width="2"/><circle cx="15" cy="15" r="4" fill="#fff" stroke="#0677BA" stroke-width="2"/><line x1="18" y1="18" x2="22" y2="22" stroke="#0677BA" stroke-width="2"/></svg></span></div>
    <div class="service" style="top:242px">Service 03<span class="service-icon"><svg width="24" height="24" viewBox="0 0 24 24"><circle cx="8" cy="14" r="3" fill="#0677BA"/><circle cx="16" cy="14" r="3" fill="#0677BA"/><path d="M3 22a5 4 0 0 1 10 0M11 22a5 4 0 0 1 10 0" fill="#0677BA"/><rect x="9" y="2" width="10" height="6" rx="1.5" fill="none" stroke="#0677BA" stroke-width="1.8"/></svg></span></div>
    <div class="service-text" style="top:106px">Description of services offered by Claravis Consulting.</div>
    <div class="service-text" style="top:180px">Highlighting our expertise in strategy, marketing, operations, and more.</div>
    <div class="service-text" style="top:254px">Examples of successful client engagements.</div>
    <div class="pattern" style="left:400px;top:90px;width:280px;height:290px" role="img" aria-label="Blue connected-dot pattern"></div>
    <div class="photo round" style="left:455px;top:160px;width:152px;height:152px;background:linear-gradient(135deg,#b89c7a,#5a4a3e)" role="img" aria-label="Photo of advisors reviewing a house model"></div>
    <div class="page-no">3</div>
  </section>
</div>

<!-- industry -->
<div class="slot" style="left:362px;top:465px">
  <section class="slide">
    <svg class="head-mark" viewBox="0 0 52 22"><line x1="0" y1="11" x2="30" y2="11" stroke="#0677BA" stroke-width="3"/><circle cx="8" cy="11" r="5" fill="#0677BA"/><circle cx="40" cy="11" r="11" fill="#0094D4"/></svg>
    <div class="slide-title">Industry Expertise</div>
    <div class="slide-sub">Navigating Consumer Goods and Services</div>
    <div class="logo"><span class="logo-dot"></span><span>CLARAVIS</span></div>
    <p class="industry-lead">Discussion on our deep understanding of the Consumer Goods and Services Industries.Showcase of industry trends and insights.<br>Case studies highlighting our industry-specific expertise.</p>
    <div class="case" style="left:26px"><h4>Case studies highlight 01</h4><p class="lorem">Discussion on our deep understanding of the Consumer Goods and Services Industries. Showcase of industry trends</p></div>
    <svg style="position:absolute;left:212px;top:194px" width="34" height="12" viewBox="0 0 34 12"><line x1="0" y1="6" x2="20" y2="6" stroke="#0677BA" stroke-width="2"/><circle cx="5" cy="6" r="3" fill="#0677BA"/><circle cx="27" cy="6" r="6" fill="#0094D4"/></svg>
    <div class="case" style="left:250px"><h4>Case studies highlight 02</h4><p class="lorem">Discussion on our deep understanding of the Consumer Goods and Services Industries. Showcase of industry trends</p></div>
    <div class="pattern" style="left:400px;top:90px;width:280px;height:290px" role="img" aria-label="Blue connected-dot pattern"></div>
    <div class="photo round" style="left:455px;top:160px;width:152px;height:152px;background:linear-gradient(160deg,#9aa3ad,#3a434f)" role="img" aria-label="Photo of glass office towers from below"></div>
    <div class="page-no">4</div>
  </section>
</div>

<!-- methodology -->
<div class="slot" style="left:40px;top:643px">
  <section class="slide">
    <svg class="head-mark" viewBox="0 0 52 22"><line x1="0" y1="11" x2="30" y2="11" stroke="#0677BA" stroke-width="3"/><circle cx="8" cy="11" r="5" fill="#0677BA"/><circle cx="40" cy="11" r="11" fill="#0094D4"/></svg>
    <div class="slide-title">Our Methodology</div>
    <div class="slide-sub">The Claravis Company Approch</div>
    <div class="logo"><span class="logo-dot"></span><span>CLARAVIS</span></div>
    <div class="step-num" style="left:92px;color:var(--navy)">01</div>
    <div class="step-num" style="left:218px;color:var(--sky)">02</div>
    <div class="step-num" style="left:342px;color:var(--soft)">03</div>
    <div class="step-num" style="left:468px;color:var(--pale)">04</div>
    <div class="step" style="left:72px;background:var(--blue);color:var(--white)">Explanation of our unique methodology. Highlighting the harmonious blend of strategy, creativity, and execution. Testimonials from satisfied clients.</div>
    <div class="step" style="left:197px;background:var(--sky);color:var(--white)">Explanation of our unique methodology. Highlighting the harmonious blend of strategy, creativity, and execution. Testimonials from satisfied clients.</div>
    <div class="step" style="left:322px;background:var(--soft);color:var(--blue)">Explanation of our unique methodology. Highlighting the harmonious blend of strategy, creativity, and execution. Testimonials from satisfied clients.</div>
    <div class="step" style="left:447px;background:var(--pale);color:var(--blue)">Explanation of our unique methodology. Highlighting the harmonious blend of strategy, creativity, and execution. Testimonials from satisfied clients.</div>
    <div class="page-no">5</div>
  </section>
</div>

<!-- team -->
<div class="slot" style="left:362px;top:643px">
  <section class="slide">
    <svg class="head-mark" viewBox="0 0 52 22"><line x1="0" y1="11" x2="30" y2="11" stroke="#0677BA" stroke-width="3"/><circle cx="8" cy="11" r="5" fill="#0677BA"/><circle cx="40" cy="11" r="11" fill="#0094D4"/></svg>
    <div class="slide-title">Meet Our Team</div>
    <div class="slide-sub">The Harmony of Expertise</div>
    <div class="logo"><span class="logo-dot"></span><span>CLARAVIS</span></div>
    <div class="member" style="left:0;background:linear-gradient(180deg,#fff 0%,#e4e6e8 50%,var(--blue) 100%)" role="img" aria-label="Portrait of a team member in a black blazer"><div class="member-label">Full Name<br>OCCUPATION</div></div>
    <div class="member" style="left:160px" role="img" aria-label="Portrait of a team member in a grey suit"><div class="member-label">Full Name<br>OCCUPATION</div></div>
    <div class="member" style="left:320px;background:linear-gradient(180deg,#e6e8ea 0%,#d8b88a 55%,var(--blue) 100%)" role="img" aria-label="Portrait of a team member in a mustard sweater"><div class="member-label">Full Name<br>OCCUPATION</div></div>
    <div class="member" style="left:480px;background:linear-gradient(180deg,#fff 0%,#c9ccd0 50%,var(--blue) 100%)" role="img" aria-label="Portrait of a team member in a dark suit"><div class="member-label">Full Name<br>OCCUPATION</div></div>
  </section>
</div>

<!-- audiences -->
<div class="slot" style="left:40px;top:820px">
  <section class="slide">
    <svg class="head-mark" viewBox="0 0 52 22"><line x1="0" y1="11" x2="30" y2="11" stroke="#0677BA" stroke-width="3"/><circle cx="8" cy="11" r="5" fill="#0677BA"/><circle cx="40" cy="11" r="11" fill="#0094D4"/></svg>
    <div class="slide-title">Target Audiences</div>
    <div class="slide-sub">Serving Diverse Clients</div>
    <div class="logo"><span class="logo-dot"></span><span>CLARAVIS</span></div>
    <div class="pattern" style="left:-20px;top:80px;width:330px;height:300px" role="img" aria-label="Blue connected-dot pattern"></div>
    <div class="photo round" style="left:75px;top:160px;width:150px;height:150px;background:linear-gradient(160deg,#6d8fa6,#2f4a60)" role="img" aria-label="Photo of a dart hitting a target"></div>
    <div class="audience" style="top:90px"><svg class="audience-icon" viewBox="0 0 26 30"><path d="M6 2a13 13 0 0 1 0 26" fill="none" stroke="#0677BA" stroke-width="2"/><circle cx="8" cy="15" r="8" fill="#0094D4"/></svg><h4>C-suite executives</h4><p>Description of how our services cater to the unique needs of each audience segment.</p></div>
    <div class="audience" style="top:170px"><svg class="audience-icon" viewBox="0 0 26 30"><path d="M6 2a13 13 0 0 1 0 26" fill="none" stroke="#0677BA" stroke-width="2"/><circle cx="8" cy="15" r="8" fill="#0094D4"/></svg><h4>industry professionals</h4><p>Description of how our services cater to the unique needs of each audience segment.</p></div>
    <div class="audience" style="top:250px"><svg class="audience-icon" viewBox="0 0 26 30"><path d="M6 2a13 13 0 0 1 0 26" fill="none" stroke="#0677BA" stroke-width="2"/><circle cx="8" cy="15" r="8" fill="#0094D4"/></svg><h4>entrepreneurs.</h4><p>Description of how our services cater to the unique needs of each audience segment.</p></div>
    <div class="page-no">7</div>
  </section>
</div>

<!-- stories -->
<div class="slot" style="left:362px;top:820px">
  <section class="slide">
    <svg class="head-mark" viewBox="0 0 52 22"><line x1="0" y1="11" x2="30" y2="11" stroke="#0677BA" stroke-width="3"/><circle cx="8" cy="11" r="5" fill="#0677BA"/><circle cx="40" cy="11" r="11" fill="#0094D4"/></svg>
    <div class="slide-title" style="font-size:33px;top:14px">Company Success Stories</div>
    <div class="slide-sub">Our Stories</div>
    <div class="logo"><span class="logo-dot"></span><span>CLARAVIS</span></div>
    <p class="story-copy">Introduction to a video showcasing successful client engagements.<br>Video footage of client testimonials, project highlights, and impactful outcomes.<br>Encouragement for the audience to watch the video to learn more about our track record of success.</p>
    <div class="story-grid">
      <div class="quote-box"><div class="quote-mark">&rdquo;</div>rem ipsum dolor sit amet, consectetuer adipiscing elit, sed diam nonumm</div>
      <div class="cell sky" role="img" aria-label="Photo of a businessman celebrating among office towers"></div>
      <div class="cell chess" role="img" aria-label="Photo of chess pieces on a board"></div>
      <div class="cell warm" role="img" aria-label="Photo of colleagues giving a high five"></div>
    </div>
    <div class="page-no">8</div>
  </section>
</div>

<!-- video -->
<div class="slot" style="left:40px;top:996px">
  <section class="slide">
    <div class="logo"><span class="logo-dot"></span><span>CLARAVIS</span></div>
    <div class="pattern" style="left:120px;top:-20px;width:400px;height:400px;background:radial-gradient(circle,rgba(255,255,255,0) 38%,rgba(0,148,212,.35) 52%,rgba(111,204,234,.2) 64%,rgba(199,235,248,0) 72%)" role="img" aria-label="Ring of blue connected dots"></div>
    <svg class="play" viewBox="0 0 40 48"><polygon points="0,0 40,24 0,48" fill="#0094D4"/></svg>
    <div class="video-label">Video go here</div>
  </section>
</div>

<!-- contact -->
<div class="slot" style="left:362px;top:996px">
  <section class="slide">
    <div class="contact-photo" role="img" aria-label="Dark photo of a desk with a laptop and documents"></div>
    <svg class="head-mark" viewBox="0 0 52 22"><line x1="0" y1="11" x2="30" y2="11" stroke="#0677BA" stroke-width="3"/><circle cx="8" cy="11" r="5" fill="#0677BA"/><circle cx="40" cy="11" r="11" fill="#0094D4"/></svg>
    <div class="contact-title">Get in Touch</div>
    <div class="contact-sub">Contact Us</div>
    <p class="contact-copy">Thank you so much for taking the time to attend our Claravis PowerPoint presentation. Your presence and engagement truly made the event a success. We value your interest in our services and hope that the insights shared during the presentation have provided you with a clearer understanding of what Claravis has to offer.</p>
    <div class="logo"><span class="logo-dot"></span><span>CLARAVIS</span></div>
    <div class="pattern" style="left:390px;top:170px;width:290px;height:220px" role="img" aria-label="Pale blue connected-dot pattern"></div>
    <dl class="contact-info">
      <dt>Our Phone number:</dt><dd>012 345 678 78</dd>
      <dt>Our Email address:</dt><dd>Youremail@email.com</dd>
      <dt>Our Website:</dt><dd>www.yourwebsite.com</dd>
    </dl>
    <div class="page-no">10</div>
  </section>
</div>

</body>
</html>
```